Brightway Talent Partners, LLC Business Card Design

Website URL: www.brightwaytalentpartners-example.com
I have attached a previous design that I find "okay" and adequate, but I wanted to explore some more distinctive/creative professional versions.
Our company provides business owners, executives and managers valuable information to help them make better people decisions. Our primary means of providing this information is through a comprehensive suite of employee assessment products across the employee life cycle that help clients better select, manage and retain talent. Company tagline is: Assess People, Predict Performance. Our employee assessment products fall into the following 3 categories:
- Assessments for Hiring Talent
- Assessments for Developing Talent
- Assessments for Retaining Talent
Please view our 3 minute overview video (link below) to get a sense of who we are:
http://videohost-example.com/q9Rt2LmXw8b
Our business personality is competent, modern, & friendly...driven by developing long lasting client relationships as opposed to one time customer transactions. We would like to see designs that are professional yet distinctive "cool business card!" and use primary logo colors/complementary color . Not sure if I prefer the gray font as shown in previous design or black...open to suggestions.
The final design should communicate competence, trust, and solutions. Also, I am an authorized business partner and consultant with two organizations that provide the assessment products I will market/use with clients. Attached are files for Meridale Worldwide and Tollard Worldwide that should be incorporated into the design (*very small but readable)

Industry/Entity Type
Business
Contact Information for Business Card
Dwight Halvers
Founder and Managing Partner
4381 North Juniper Mill Lane
Suite 715
Atlanta GA 30419-5183
Office: 555.014.2796
dhalvers@brightwaytalentpartners-example.com
www.brightwaytalentpartnrs-example.com

```html
<!DOCTYPE html>
<html lang="en">
<head>
<meta charset="utf-8">
<title>Brightway Talent Partners – Business Card</title>
<link rel="stylesheet" href="https://fonts.googleapis.com/css2?family=Source+Sans+3:wght@400;600&display=swap">
<style>
  :root {
    --page-bg: #e4e4e4;
    --card-bg: #ffffff;
    --brand-purple: #33175a;
    --brand-blue: #3f6fb8;
    --globe-blue: #5b8fd6;
    --text-gray: #444446;
    --rule-gray: #b9b9bd;
    --badge-warm: #d9d2c8;
    --badge-cool: #cfdcee;
  }
  * { margin: 0; padding: 0; box-sizing: border-box; }
  html, body {
    width: 1200px; height: 840px; overflow: hidden;
    background: var(--page-bg);
    font-family: "Source Sans 3", "Myriad Pro", Arial, sans-serif;
  }
  .card {
    position: absolute; left: 100px; top: 136px;
    width: 1000px; height: 568px;
    background: var(--card-bg);
    overflow: hidden;
  }
  .brand-mark {
    position: absolute; left: 186px; top: 74px;
    width: 96px; height: 96px; border-radius: 50%;
    background: var(--globe-blue);
  }
  .brand-name {
    position: absolute; left: 72px; top: 184px;
    font-size: 34px; font-weight: 600; color: var(--brand-purple);
    letter-spacing: -0.3px; line-height: 44px; white-space: nowrap;
  }
  .tagline {
    position: absolute; left: 73px; top: 234px;
    font-size: 17px; line-height: 22px; color: var(--brand-blue); white-space: nowrap;
  }
  .person {
    position: absolute; right: 71px; top: 274px; text-align: right;
  }
  .person-name { font-size: 31px; font-weight: 600; color: var(--brand-purple); line-height: 1.1; }
  .person-title { font-size: 23px; color: var(--brand-blue); line-height: 1.4; }
  .divider {
    position: absolute; left: 72px; top: 351px;
    width: 857px; height: 2px; background: var(--rule-gray);
  }
  .address {
    position: absolute; left: 72px; top: 366px;
    font-size: 24px; line-height: 34px; color: var(--text-gray); font-style: normal;
  }
  .contact {
    position: absolute; left: 72px; top: 442px;
    font-size: 22px; line-height: 36px; color: var(--text-gray);
    list-style: none;
  }
  .contact li { display: flex; align-items: center; gap: 8px; white-space: nowrap; }
  .contact svg { width: 22px; height: 22px; fill: var(--brand-purple); flex: none; }
  .contact .email { font-size: 20px; }
  .partner-badges {
    position: absolute; right: 71px; top: 452px;
    display: flex; gap: 14px;
  }
  .partner-badge { width: 176px; height: 48px; border-radius: 4px; }
  .partner-badge.tollard { background: var(--badge-warm); }
  .partner-badge.meridale { background: var(--badge-cool); }
  .footer-band { position: absolute; left: 0; bottom: 0; width: 1000px; height: 54px; }
  .website {
    position: absolute; right: 71px; bottom: 13px;
    font-size: 20px; line-height: 26px; font-weight: 600; color: #ffffff; white-space: nowrap;
  }
</style>
</head>
<body>
  <main class="card">
    <div class="brand-mark"></div>
    <div class="brand-name">Brightway Talent Partners</div>
    <div class="tagline">Measure Talent &bull; Forecast Success</div>

    <div class="person">
      <div class="person-name">Dwight Halvers</div>
      <div class="person-title">Founder and Managing Partner</div>
    </div>

    <div class="divider"></div>

    <address class="address">
      4381 North Juniper Mill Lane<br>
      Suite 715 Atlanta GA 30419-5183
    </address>

    <ul class="contact">
      <li>
        <svg viewBox="0 0 24 24" aria-hidden="true"><path d="M6.6 10.8a15.1 15.1 0 0 0 6.6 6.6l2.2-2.2c.3-.3.7-.4 1-.2 1.1.4 2.3.6 3.6.6.6 0 1 .4 1 1V20c0 .6-.4 1-1 1A17 17 0 0 1 3 4c0-.6.4-1 1-1h3.5c.6 0 1 .4 1 1 0 1.3.2 2.5.6 3.6.1.3 0 .7-.2 1z"/></svg>
        555.014.2796
      </li>
      <li class="email">
        <svg viewBox="0 0 24 24" aria-hidden="true"><path d="M2 5h20v14H2z M4 7v.4l8 5.2 8-5.2V7z" fill-rule="evenodd"/></svg>
        dhalvers@brightwaytalentpartners-example.com
      </li>
    </ul>

    <div class="partner-badges">
      <div class="partner-badge tollard" role="img" aria-label="Tollard Worldwide certified consultant badge"></div>
      <div class="partner-badge meridale" role="img" aria-label="Meridale Worldwide authorized business partner badge"></div>
    </div>

    <svg class="footer-band" viewBox="0 0 1000 54" preserveAspectRatio="none" aria-hidden="true">
      <rect x="0" y="12" width="560" height="42" fill="var(--brand-purple)"/>
      <path d="M490 54 C505 30 520 9 565 9 L1000 9 L1000 54 Z" fill="#ffffff"/>
      <path d="M500 54 C515 32 530 14 572 14 L1000 14 L1000 54 Z" fill="var(--brand-blue)"/>
    </svg>
    <div class="website">www.brightwaytalentpartnrs-example.com</div>
  </main>
</body>
</html>
```